Website Design for Harbor 7340

We need a website design for a new company that strives to provide training and structure for religious missionaries who are traveling the world to teach of christianity.
They provide training in:
- Nutrition Coaching & Daily assignments
- Personal Training Sessions
- Phycological emotional/mental component
The goal of Harbor 7340 is to help missionaries preach the gospel of christ to those who haven't heard it due to geographical obstacles and physical limitations that get in the way.
The homepage template has linked images to use. If any other images are needed, stock images are acceptable.

Logo/Color Scheme: https://files.quorvex.net/share/8Kd2Lm9XpQ4rTz7WvN3bYc6HsJ1aFe0Gu

Customer Avatar/Core Message Canvas: https://sheets.plendora.net/s/4Rq81ZtyMn2wXcVb7KpLd0HsJ9aFgE3QuTo6YiPxNe/view

Homepage Template: https://docs.plendora.net/d/7Nw52KxpTr8vYzQm3LcBf1GhJ6dSeA0RuWo4XiZqPk/view

```html
<!DOCTYPE html>
<html lang="en">
<head>
<meta charset="utf-8">
<title>Harbor 7340 – Mind + Body + Spirit</title>
<link href="https://fonts.googleapis.com/css2?family=Bebas+Neue&family=Lato:wght@400;700&display=swap" rel="stylesheet">
<style>
:root{
  --gold:#e2b740;
  --gold-deep:#caa032;
  --olive:#2f3a20;
  --olive-soft:#434d30;
  --ink:#1b1b1b;
  --paper:#f7f5f5;
  --white:#ffffff;
  --black:#050505;
}
*{box-sizing:border-box;margin:0;padding:0}
html,body{width:1200px;height:4573px;overflow:hidden;background:var(--white)}
body{font-family:'Lato',sans-serif;color:var(--ink)}
.page{position:relative;width:1200px;height:4573px;overflow:hidden}
.abs{position:absolute}
.display{font-family:'Bebas Neue',sans-serif;font-weight:400;letter-spacing:.5px}
.hl{color:var(--gold)}
.center{text-align:center;left:0;width:1200px}
.rule{position:absolute;left:517px;width:166px;height:2px;background:#bdbdbd}
.rule::after{content:"";position:absolute;left:56px;top:-2px;width:54px;height:6px;background:var(--gold)}
.btn{position:absolute;font-family:'Bebas Neue',sans-serif;font-size:20px;display:flex;align-items:center;justify-content:center;border-radius:8px}
.btn-gold{background:var(--gold);color:var(--olive);box-shadow:0 0 0 3px rgba(226,183,64,.35)}
.btn-olive{background:var(--olive);color:var(--white);box-shadow:0 0 0 3px rgba(47,58,32,.35)}

/* hero */
.hero-frame{left:0;top:0;width:1200px;height:652px;background:var(--gold);
  clip-path:polygon(0 0,100% 0,100% 540px,1090px 652px,110px 652px,0 540px)}
.hero-photo{left:0;top:0;width:1200px;height:646px;
  background:linear-gradient(160deg,#1f3550 0%,#41607c 30%,#7a8ca0 50%,#6b5a3a 75%,#3a2f1c 100%);
  clip-path:polygon(0 0,100% 0,100% 536px,1088px 646px,112px 646px,0 536px)}
.header{left:107px;top:0;width:985px;height:85px;background:var(--white);border-radius:0 0 30px 30px}
.brand{position:absolute;left:30px;top:14px;font-family:'Bebas Neue',sans-serif;font-size:50px;color:var(--olive);line-height:56px}
.nav{position:absolute;left:400px;top:32px;display:flex;gap:22px;font-family:'Bebas Neue',sans-serif;font-size:19px;color:var(--ink)}
.signup{left:833px;top:20px;width:122px;height:46px;background:var(--olive);color:var(--gold);border-radius:10px;font-size:19px;gap:8px}
.hero-title{left:110px;top:168px;font-size:50px;line-height:73px;color:var(--white);width:620px}
.hero-text{left:110px;top:390px;width:520px;font-size:14px;line-height:27px;color:var(--white)}
.hero-arrow{width:36px;height:36px;border-radius:50%;background:var(--white);top:330px;display:flex;align-items:center;justify-content:center}

/* staff */
.section-title{font-size:44px;line-height:60px;color:var(--ink)}
.staff{width:180px;text-align:center}
.staff svg{display:block;margin:0 auto}
.staff .label{font-family:'Bebas Neue',sans-serif;font-size:21px;margin-top:18px}

/* why */
.why-band{left:0;top:1381px;width:1200px;height:609px;
  background:linear-gradient(135deg,#2c3520 0%,#3f4a2c 45%,#2a321d 100%);
  clip-path:polygon(110px 0,1090px 0,1200px 90px,1200px 100%,0 100%,0 90px)}
.why-copy{left:160px;width:880px;color:var(--white);font-size:14.5px;line-height:29px;text-align:center}

/* approach */
.octa-side .label{font-family:'Bebas Neue',sans-serif;font-size:24px;text-align:center;margin-top:24px}
.mind-copy{left:440px;top:2455px;width:320px;color:var(--white);font-size:14px;line-height:26px;text-align:center}

/* who */
.who-band{left:0;top:2799px;width:1200px;height:730px;background:var(--gold);
  clip-path:polygon(110px 0,1090px 0,1200px 90px,1200px calc(100% - 90px),1090px 100%,110px 100%,0 calc(100% - 90px),0 90px)}
.card{width:296px;height:397px;background:var(--white);padding:8px}
.card .photo{width:280px;height:216px}
.card .cap{position:relative;margin:-26px 16px 0;background:var(--white);padding-top:10px;text-align:center}
.card h3{font-family:'Bebas Neue',sans-serif;font-weight:400;font-size:21px;line-height:27px;color:var(--olive)}
.card p{font-size:12.5px;line-height:26px;margin-top:4px}
.card .more{font-family:'Bebas Neue',sans-serif;font-size:17px;text-decoration:underline;margin-top:6px;display:block;color:var(--ink)}

/* newsletter */
.news-bg{left:0;top:3529px;width:1200px;height:600px;background:var(--paper)}
.email{left:192px;top:3905px;width:814px;height:53px;background:var(--white);border-radius:27px;box-shadow:0 2px 8px rgba(0,0,0,.12);padding-left:30px;display:flex;align-items:center;font-size:14px;color:#666}

/* footer */
.foot-frame{left:0;top:4123px;width:1200px;height:450px;background:var(--gold);
  clip-path:polygon(110px 0,1090px 0,1200px 90px,1200px 100%,0 100%,0 90px)}
.foot{left:0;top:4129px;width:1200px;height:444px;background:var(--black);
  clip-path:polygon(112px 0,1088px 0,1200px 92px,1200px 100%,0 100%,0 92px)}
.foot-brand{left:110px;top:4226px;font-family:'Bebas Neue',sans-serif;font-size:58px;color:var(--white);line-height:62px}
.social{top:4335px;width:30px;height:30px;border-radius:50%;background:var(--gold)}
.foot-h{font-family:'Bebas Neue',sans-serif;font-size:22px;color:var(--white)}
.foot-list{list-style:none;color:var(--white);font-size:14px}
.foot-list li{display:flex;align-items:center;gap:10px;height:35px}
.chev{width:14px;height:14px;border-radius:50%;background:var(--white);display:flex;align-items:center;justify-content:center}
.contact{display:flex;gap:14px;color:var(--white);font-size:14px;line-height:26px}
.cicon{width:30px;height:30px;border-radius:50%;background:var(--gold);display:flex;align-items:center;justify-content:center;flex:none}
</style>
</head>
<body>
<div class="page">

  <!-- HERO -->
  <div class="abs hero-frame"></div>
  <div class="abs hero-photo" role="img" aria-label="Hikers with backpacks climbing a sunlit mountain ridge above a lake"></div>

  <header class="abs header">
    <div class="brand">Harbor 7340</div>
    <nav class="nav"><span>Programs</span><span>Events</span><span>Online Store</span><span>About Us</span><span>Contact Us</span></nav>
    <div class="btn signup" style="position:absolute">
      <svg width="22" height="22" viewBox="0 0 24 24" fill="none" stroke="#e2b740" stroke-width="2"><rect x="4" y="3" width="14" height="18" rx="2"/><path d="M8 8h6M8 12h6M8 16h3"/></svg>Sign Up
    </div>
  </header>

  <h1 class="abs display hero-title">Empowing Change: <span class="hl">By Illuminating Lives Unexposed</span> to the Gospel’s Light</h1>
  <p class="abs hero-text">Harbor 7340’s mission is to enable the word of Jesus to be experienced by people in the most remote and treacherous parts of the world.</p>
  <div class="btn" style="left:110px;top:465px;width:170px;height:52px;border:2px solid #fff;color:#fff;border-radius:10px">View Our Programs</div>
  <div class="btn btn-gold" style="left:308px;top:465px;width:198px;height:52px;border-radius:10px">Register for Training</div>
  <div class="abs hero-arrow" style="left:30px"><svg width="14" height="14" viewBox="0 0 14 14"><path d="M9 2 4 7l5 5" stroke="#222" stroke-width="2.4" fill="none"/></svg></div>
  <div class="abs hero-arrow" style="left:1127px"><svg width="14" height="14" viewBox="0 0 14 14"><path d="M5 2l5 5-5 5" stroke="#222" stroke-width="2.4" fill="none"/></svg></div>

  <!-- STAFF -->
  <h2 class="abs center display section-title" style="top:698px">Harbor 7340<span class="hl">’s Well-Rounded Staff</span> For<br>Specialized Training</h2>
  <div class="rule" style="top:833px"></div>

  <div class="abs staff" style="left:98px;top:884px"><svg width="155" height="155" viewBox="0 0 100 100" role="img" aria-label="Pastor icon"><polygon points="29,0 71,0 100,29 100,71 71,100 29,100 0,71 0,29" fill="#e2b740"/><polygon points="31,6 69,6 94,31 94,69 69,94 31,94 6,69 6,31" fill="none" stroke="#2f3a20" stroke-width="1.4"/></svg><div class="label">Pastor</div></div>
  <div class="abs staff" style="left:304px;top:884px"><svg width="155" height="155" viewBox="0 0 100 100" role="img" aria-label="Former ranger icon"><polygon points="29,0 71,0 100,29 100,71 71,100 29,100 0,71 0,29" fill="#e2b740"/><polygon points="31,6 69,6 94,31 94,69 69,94 31,94 6,69 6,31" fill="none" stroke="#2f3a20" stroke-width="1.4"/></svg><div class="label">Former Ranger</div></div>
  <div class="abs staff" style="left:510px;top:884px"><svg width="155" height="155" viewBox="0 0 100 100" role="img" aria-label="Nutritionist icon"><polygon points="29,0 71,0 100,29 100,71 71,100 29,100 0,71 0,29" fill="#e2b740"/><polygon points="31,6 69,6 94,31 94,69 69,94 31,94 6,69 6,31" fill="none" stroke="#2f3a20" stroke-width="1.4"/></svg><div class="label">Nutritionist</div></div>
  <div class="abs staff" style="left:716px;top:884px"><svg width="155" height="155" viewBox="0 0 100 100" role="img" aria-label="Dietician icon"><polygon points="29,0 71,0 100,29 100,71 71,100 29,100 0,71 0,29" fill="#e2b740"/><polygon points="31,6 69,6 94,31 94,69 69,94 31,94 6,69 6,31" fill="none" stroke="#2f3a20" stroke-width="1.4"/></svg><div class="label">Dietician</div></div>
  <div class="abs staff" style="left:922px;top:884px"><svg width="155" height="155" viewBox="0 0 100 100" role="img" aria-label="Psychologist icon"><polygon points="29,0 71,0 100,29 100,71 71,100 29,100 0,71 0,29" fill="#e2b740"/><polygon points="31,6 69,6 94,31 94,69 69,94 31,94 6,69 6,31" fill="none" stroke="#2f3a20" stroke-width="1.4"/></svg><div class="label">Psychologist</div></div>
  <div class="abs staff" style="left:286px;top:1113px"><svg width="155" height="155" viewBox="0 0 100 100" role="img" aria-label="Former special ops icon"><polygon points="29,0 71,0 100,29 100,71 71,100 29,100 0,71 0,29" fill="#e2b740"/><polygon points="31,6 69,6 94,31 94,69 69,94 31,94 6,69 6,31" fill="none" stroke="#2f3a20" stroke-width="1.4"/></svg><div class="label">Former Special Ops</div></div>
  <div class="abs staff" style="left:510px;top:1113px"><svg width="155" height="155" viewBox="0 0 100 100" role="img" aria-label="Professional trainer icon"><polygon points="29,0 71,0 100,29 100,71 71,100 29,100 0,71 0,29" fill="#e2b740"/><polygon points="31,6 69,6 94,31 94,69 69,94 31,94 6,69 6,31" fill="none" stroke="#2f3a20" stroke-width="1.4"/></svg><div class="label">Professional Trainer</div></div>
  <div class="abs staff" style="left:734px;top:1113px"><svg width="155" height="155" viewBox="0 0 100 100" role="img" aria-label="Former special ops icon"><polygon points="29,0 71,0 100,29 100,71 71,100 29,100 0,71 0,29" fill="#e2b740"/><polygon points="31,6 69,6 94,31 94,69 69,94 31,94 6,69 6,31" fill="none" stroke="#2f3a20" stroke-width="1.4"/></svg><div class="label">Former Special Ops</div></div>

  <!-- WHY -->
  <div class="abs why-band" role="img" aria-label="Dark olive-toned photo of hands holding an open Bible"></div>
  <h2 class="abs center display hl" style="top:1448px;font-size:44px;line-height:54px">Why Harbor 7340 is Breaking Barriers</h2>
  <div class="rule" style="top:1525px"></div>
  <p class="abs why-copy" style="top:1558px">Geographical challenges make some communities difficult for missionaries to reach. The Harbor 7340 program is designed to remove the physical limitations that can hinder us from bringing the Gospel to places that seem physically impossible to reach. Harbor 7340 is founded on Romans 15:20.</p>
  <p class="abs why-copy" style="top:1674px">In his letter to the Romans, Paul requests funding to take the Gospel to Spain. In this letter, he writes: “[20] and thus I make it my ambition to preach the gospel, not where Christ has already been named, lest I build on someone else’s foundation, [21] but it is written, “those who have never been told of him will see, and those who have never heard will understand.”</p>
  <div class="abs center display hl" style="top:1812px;font-size:17px">[Romans 15:20-21]</div>
  <div class="btn btn-gold" style="left:519px;top:1868px;width:162px;height:48px">Join Our Mission</div>

  <!-- APPROACH -->
  <h2 class="abs center display section-title" style="top:2047px">Harbor <span class="hl">7340 Missionary Training</span> Approach<br>Mind - Body - Spirit</h2>
  <div class="rule" style="top:2187px"></div>

  <div class="abs octa-side" style="left:110px;top:2285px;width:225px"><svg width="225" height="225" viewBox="0 0 100 100" role="img" aria-label="Body icon"><polygon points="29,0 71,0 100,29 100,71 71,100 29,100 0,71 0,29" fill="#e2b740"/></svg><div class="label">Body</div></div>
  <div class="abs octa-side" style="left:863px;top:2285px;width:225px"><svg width="225" height="225" viewBox="0 0 100 100" role="img" aria-label="Spirit dove icon"><polygon points="29,0 71,0 100,29 100,71 71,100 29,100 0,71 0,29" fill="#e2b740"/></svg><div class="label">Spirit</div></div>
  <svg class="abs" style="left:405px;top:2222px" width="390" height="390" viewBox="0 0 100 100"><polygon points="29,0 71,0 100,29 100,71 71,100 29,100 0,71 0,29" fill="#2f3a20"/><polygon points="30.5,3.5 69.5,3.5 96.5,30.5 96.5,69.5 69.5,96.5 30.5,96.5 3.5,69.5 3.5,30.5" fill="none" stroke="#e2b740" stroke-width=".6"/></svg>
  <div class="abs" style="left:555px;top:2262px;width:90px;height:90px;border-radius:12px;background:#4a5536" role="img" aria-label="Mind icon of a head with radiating lines"></div>
  <div class="abs" style="left:490px;top:2360px;width:220px;height:60px;border-radius:30px 30px 10px 10px;background:linear-gradient(#3a4528,#2f3a20)" role="img" aria-label="Faint open hands decoration"></div>
  <div class="abs center display" style="top:2400px;font-size:34px;color:#fff">Mind</div>
  <p class="abs mind-copy">Psychologically, we will prepare the mind through counseling, breathing techniques, and simulations in order to prepare for psychological challenges that come with being in the field.</p>
  <div class="btn btn-gold" style="left:451px;top:2673px;width:298px;height:48px">View Our Detailed Training Program</div>

  <!-- WHO -->
  <div class="abs who-band"></div>
  <h2 class="abs center display" style="top:2852px;font-size:46px;color:var(--olive)">Who is Harbor 7340 For?</h2>
  <div class="abs" style="left:517px;top:2932px;width:166px;height:2px;background:#8a7a3c"></div>
  <div class="abs" style="left:573px;top:2930px;width:54px;height:6px;background:var(--olive)"></div>

  <div class="abs card" style="left:112px;top:2968px">
    <div class="photo" role="img" aria-label="Group of people walking single file along a village path" style="background:linear-gradient(180deg,#9fb4c8,#5f7a52 55%,#6b5a3c)"></div>
    <div class="cap"><h3>Sending<br>Agencies for Missionaries</h3><p>Are you looking to improve the training you’re offering your flock? We have designed a program to align our training with your goals</p><span class="more">Read More</span></div>
  </div>
  <div class="abs card" style="left:452px;top:2968px">
    <div class="photo" role="img" aria-label="Hand holding a small red Bible in front of a globe" style="background:linear-gradient(135deg,#b9c7d3,#6f8fa6 55%,#8b2a2a)"></div>
    <div class="cap"><h3>Missionaries</h3><p>Are you independently seeking to develop your knowledge and skills independently? We are here to help! We can customize a training approach that fits your specific needs.</p><span class="more">Read More</span></div>
  </div>
  <div class="abs card" style="left:792px;top:2968px">
    <div class="photo" role="img" aria-label="Hands resting on an open Bible in warm light" style="background:linear-gradient(135deg,#3a2a1c,#a0703e 55%,#d9c3a0)"></div>
    <div class="cap"><h3>Christian-Based<br>Training Program for All!</h3><p>Are you looking to support the missionary community? Well we have a solution for you! We also offer a customized, personal-training approach for everyone</p><span class="more">Read More</span></div>
  </div>
  <div class="btn btn-olive" style="left:485px;top:3420px;width:230px;height:48px">View Our Training Options</div>

  <!-- NEWSLETTER -->
  <div class="abs news-bg"></div>
  <h2 class="abs center display section-title" style="top:3600px">Join Our Missionary Training: <span class="hl">Stay Up-To-Date on Our<br>Training Programs, Missionary Success Stories,</span><br>and New Program Info!</h2>
  <div class="rule" style="top:3799px"></div>
  <p class="abs center" style="top:3826px;font-size:14px;line-height:26px">Subscribe and help us in supporting our missionaries as they spread the Gospel to all corners and<br>areas of the world</p>
  <div class="abs email">Enter The Email</div>
  <div class="btn btn-gold" style="left:532px;top:4006px;width:136px;height:48px">Subscribe</div>

  <!-- FOOTER -->
  <div class="abs foot-frame"></div>
  <div class="abs foot"></div>
  <div class="abs foot-brand">Harbor 7340</div>
  <div class="abs social" style="left:113px"></div>
  <div class="abs social" style="left:171px"></div>
  <div class="abs social" style="left:229px"></div>
  <div class="abs social" style="left:287px"></div>

  <div class="abs foot-h" style="left:469px;top:4226px">Quick Links</div>
  <ul class="abs foot-list" style="left:469px;top:4264px">
    <li><span class="chev"><svg width="8" height="8" viewBox="0 0 8 8"><path d="M3 1l3 3-3 3" stroke="#000" stroke-width="1.6" fill="none"/></svg></span>Programs</li>
    <li><span class="chev"><svg width="8" height="8" viewBox="0 0 8 8"><path d="M3 1l3 3-3 3" stroke="#000" stroke-width="1.6" fill="none"/></svg></span>Events</li>
    <li><span class="chev"><svg width="8" height="8" viewBox="0 0 8 8"><path d="M3 1l3 3-3 3" stroke="#000" stroke-width="1.6" fill="none"/></svg></span>Online Store</li>
    <li><span class="chev"><svg width="8" height="8" viewBox="0 0 8 8"><path d="M3 1l3 3-3 3" stroke="#000" stroke-width="1.6" fill="none"/></svg></span>About Us</li>
    <li><span class="chev"><svg width="8" height="8" viewBox="0 0 8 8"><path d="M3 1l3 3-3 3" stroke="#000" stroke-width="1.6" fill="none"/></svg></span>Contact Us</li>
  </ul>

  <div class="abs foot-h" style="left:666px;top:4226px">Help Links</div>
  <ul class="abs foot-list" style="left:666px;top:4264px">
    <li><span class="chev"><svg width="8" height="8" viewBox="0 0 8 8"><path d="M3 1l3 3-3 3" stroke="#000" stroke-width="1.6" fill="none"/></svg></span>FAQ</li>
    <li><span class="chev"><svg width="8" height="8" viewBox="0 0 8 8"><path d="M3 1l3 3-3 3" stroke="#000" stroke-width="1.6" fill="none"/></svg></span>Terms of Service</li>
    <li><span class="chev"><svg width="8" height="8" viewBox="0 0 8 8"><path d="M3 1l3 3-3 3" stroke="#000" stroke-width="1.6" fill="none"/></svg></span>Privacy Policy</li>
    <li><span class="chev"><svg width="8" height="8" viewBox="0 0 8 8"><path d="M3 1l3 3-3 3" stroke="#000" stroke-width="1.6" fill="none"/></svg></span>Case Studies</li>
    <li><span class="chev"><svg width="8" height="8" viewBox="0 0 8 8"><path d="M3 1l3 3-3 3" stroke="#000" stroke-width="1.6" fill="none"/></svg></span>Miscellaneous Information</li>
  </ul>

  <div class="abs foot-h" style="left:907px;top:4226px">Contact Us</div>
  <div class="abs contact" style="left:907px;top:4270px">
    <span class="cicon"><svg width="14" height="16" viewBox="0 0 14 16"><path d="M7 15s5-5 5-9A5 5 0 0 0 2 6c0 4 5 9 5 9z" fill="#000"/><circle cx="7" cy="6" r="2" fill="#e2b740"/></svg></span>
    <span>Harbor 7340<br>United States</span>
  </div>
  <div class="abs contact" style="left:907px;top:4336px;align-items:center">
    <span class="cicon"><svg width="14" height="14" viewBox="0 0 24 24"><path d="M6.6 10.8a15 15 0 0 0 6.6 6.6l2.2-2.2a1 1 0 0 1 1-.25 11 11 0 0 0 3.6.6 1 1 0 0 1 1 1V20a1 1 0 0 1-1 1A17 17 0 0 1 3 4a1 1 0 0 1 1-1h3.5a1 1 0 0 1 1 1 11 11 0 0 0 .6 3.6 1 1 0 0 1-.25 1z" fill="#000"/></svg></span>
    <span>+1 555 014 7340</span>
  </div>
  <div class="abs contact" style="left:907px;top:4388px;align-items:center">
    <span class="cicon"><svg width="14" height="12" viewBox="0 0 14 12"><rect x="1" y="1" width="12" height="10" rx="1" fill="#000"/><path d="M1.5 2l5.5 4.5L12.5 2" stroke="#e2b740" stroke-width="1.2" fill="none"/></svg></span>
    <span>info@harbor7340.com</span>
  </div>

  <div class="abs" style="left:110px;top:4486px;width:980px;height:1px;background:#8a8a8a"></div>
  <div class="abs center" style="top:4520px;font-size:14px;color:#fff">Copyrights@2023 Harbor 7340. All Rights Reserved</div>

</div>
</body>
</html>
```